Wordpress design for my private practice website - Psychotherapist

I would like a simple, clean, and elegant design for my private practice website. I work with both adults and children so I'd like it to appeal to both. However, since parents make the choice as to where to send their child for therapy, I want it to appeal to adults more. I would like the pictures on the site to have a calming effect - maybe using sand and water and rocks. I am attaching files with my company logo. I would also like my name incorporated into the header - Colette Brannigan, LCSW, Registered Play Therapist. I've also uploaded a picture of myself for my About Page.

I like the design of these 2 website and want something similar:
www.drlorapenwick.example
www.harwood-tallis.example

I would like a home page that highlights a calming graphic across the entire top of the page as well as my practice logo and my name.

I'd like a link to social media sites on the top of the homepage - facebook, pinterest.

I want a simple bar across the top with the following tabs:
Home
About Me (subtabs Who I Am, Specialties and Approach)
Counseling Services (subtabs Individual Counseling, Play Therapy, Sandplay Therapy,)
Fees
FAQs
Contact Me (would love this to be a fill in the blank contact form that sends info to my email address - should include name, phone number, email and a comment box for more information requested)
Blog (this will link with another wordpress blog)

Target Market(s)

Parents of children under age 12 with behavioral problems or are dealing with the breakup of their family through divorce - looking for someone to work with their young child. I also work with Adults that are overwhelmed and worried - often women that have many life stressors and are feeling burnt out on life and meeting everyone's needs. Families going through some type of trauma, including divorce or grief work. I also work with individuals going through a transition of religious beliefs - often exiting the religion of their youth and undergoing a crisis of faith at midlife.

Industry/Entity Type

Mental Health

Contact Information for Business Card

Colette Brannigan, LCSW
Registered Play Therapist
4917 Wexmoor Lane
Idaho Falls, Idaho 83404
(208)555-0187
www.stillbrookcounseling.example

On the opposite side, I'd like an appointment reminder area - with the following text:

Your next appointment is
_____/______/______ at ______am/pm
Please give 24 hrs notice if you need to cancel your appointment.

Coding

Coded - Design and coding required

Number of Pages Required

5+ page

Font styles to use
Sans Serif

Colors
33a6d7
9bcb3c
0355a3

Requirements
Must have
• I'd like it to be a wordpress site. I'm such a newby at web design - but I need to be able to add content and manage the site myself once it is up and running.
Nice to have
• I like the design of these 2 websites and want something similar:
• www.drlorapenwick.example
• www.harwood-tallis.example
• They are clean, easy to navigate and calming.
Should not have
• Should not look like a childcare website.

```html
<!DOCTYPE html>
<html lang="en">
<head>
<meta charset="utf-8">
<title>Stillbrook Counseling</title>
<link rel="stylesheet" href="https://fonts.googleapis.com/css2?family=PT+Sans:ital,wght@0,400;0,700;1,400;1,700&family=Source+Sans+3:wght@300;400&display=swap">
<style>
:root{
  --blue:#0355a3;
  --sky:#33a6d7;
  --green:#9bcb3c;
  --ink:#5f5f5f;
  --soft-ink:#8a8a8a;
  --welcome-bg:#dfeaf0;
  --quote-bg:#f4f0f0;
  --footer-bg:#d2d2d2;
  --footer-bar:#9b9b9b;
  --white:#ffffff;
}
*{box-sizing:border-box;margin:0;padding:0}
html,body{width:906px;height:1200px;overflow:hidden}
body{position:relative;font-family:"PT Sans",Arial,sans-serif;color:var(--ink);background:var(--white)}
.abs{position:absolute}

.hero{left:0;top:0;width:906px;height:378px;
  background:
    radial-gradient(circle at 68% 48%,#9fd1b8 0,#7fb8a3 18%,transparent 34%),
    radial-gradient(circle at 22% 30%,#d58aa6 0,transparent 22%),
    radial-gradient(circle at 88% 85%,#d46a8c 0,transparent 20%),
    radial-gradient(circle at 40% 80%,#8ec4b4 0,transparent 25%),
    linear-gradient(135deg,#6d9a8c,#b97993 55%,#5e8f82)}
.hero-band{left:0;top:152px;width:906px;height:187px;background:rgba(40,40,45,.32)}
.hero-brand{left:134px;top:270px;width:240px;text-align:center;color:var(--white);font-family:"Source Sans 3",sans-serif;font-weight:300}
.hero-brand .mark{display:block;width:34px;height:34px;border-radius:50%;background:var(--white);margin:0 auto 16px}
.hero-brand .name{display:block;font-size:22px;letter-spacing:7px}
.hero-brand .sub{display:block;font-size:11px;letter-spacing:5px;margin-top:6px}

.topbar{left:0;top:0;width:906px;height:55px;background:rgba(240,240,240,.82)}
.top-brand{left:86px;top:14px;width:76px;text-align:center;font-family:"PT Sans",sans-serif;font-size:7px;letter-spacing:1.5px;color:var(--blue)}
.top-brand .dot{display:block;width:14px;height:14px;border-radius:50%;background:var(--blue);margin:0 auto 4px}
.practitioner{left:178px;top:12px;font-size:13px;line-height:15px;color:#6a6a6a}
.nav{left:398px;top:19px;display:flex;gap:21px;list-style:none;font-size:12.5px;color:#555}
.nav li{position:relative}
.nav li.active::before{content:"";position:absolute;left:1px;top:-19px;width:28px;height:3px;background:var(--sky)}

.welcome{left:0;top:378px;width:906px;height:164px;background:var(--welcome-bg)}
.welcome h1{position:absolute;left:0;top:46px;width:906px;text-align:center;font-family:"Source Sans 3",sans-serif;font-weight:400;font-size:29px;letter-spacing:5.5px;color:#707070}
.welcome .rule{position:absolute;left:123px;top:92px;width:659px;height:5px;border-top:1px solid #8c97a0;border-bottom:1px solid #8c97a0}
.welcome p{position:absolute;left:0;top:104px;width:906px;text-align:center;font-size:13px;line-height:16px;color:#6c6c6c}

.portrait{left:129px;top:578px;width:250px;height:366px;background:linear-gradient(180deg,#bcbcbc,#8e8e8e 60%,#5a5a5a)}

.section-title{font-family:"Source Sans 3",sans-serif;font-size:15px;color:#444;display:flex;align-items:center;gap:6px}
.section-title::after{content:"";flex:1;height:3px;border-top:1px solid #ddd;border-bottom:1px solid #ddd}
.services-title{left:482px;top:580px;width:316px}
.services{left:481px;top:613px;list-style:none;font-size:8px;color:#666}
.services li{display:flex;align-items:center;gap:8px;height:22px}
.services svg{width:11px;height:11px;flex:none}

.clients-title{left:476px;top:771px;width:296px}
.quote{left:479px;top:808px;width:293px;height:97px;background:var(--quote-bg);padding:14px 16px;font-size:7.4px;line-height:13px;font-style:italic;color:#666}
.quote::after{content:"";position:absolute;left:26px;bottom:-10px;border-left:0 solid transparent;border-right:14px solid transparent;border-top:10px solid var(--quote-bg)}
.author{left:479px;top:911px;display:flex;align-items:center;gap:10px;font-size:7.5px;font-weight:700;color:#333}

.gap-band{left:0;top:966px;width:906px;height:8px;background:#ececec}
.footer{left:0;top:974px;width:906px;height:187px;background:var(--footer-bg)}
.foot-brand{left:174px;top:22px;width:140px;text-align:center;color:#7a7a7a}
.foot-brand .dot{display:block;width:30px;height:30px;border-radius:50%;background:var(--blue);margin:0 auto 10px}
.foot-brand .name{display:block;font-size:12px;letter-spacing:3px}
.foot-brand .sub{display:block;font-size:7px;letter-spacing:2.5px;margin-top:2px}
.foot-blurb{left:178px;top:110px;width:140px;font-size:7.6px;line-height:13px;font-style:italic;font-weight:700;color:#777}
.foot-heading{font-size:17px;color:#888;font-family:"Source Sans 3",sans-serif}
.contact{left:409px;top:18px;font-size:12px;color:#888;line-height:17.5px}
.contact .foot-heading{margin-bottom:12px}
.contact p+p{margin-top:17px}
.menu{left:655px;top:14px}
.menu ul{list-style:none;margin-top:12px;font-size:13.5px;line-height:17.5px;color:#888}

.bottom-bar{left:0;top:1161px;width:906px;height:39px;background:var(--footer-bar)}
.copyright{left:149px;top:14px;font-size:7px;color:var(--white)}
.social{left:648px;top:14px;display:flex;gap:13px}
.social span{display:block;width:10px;height:10px;border-radius:50%;background:#555}
</style>
</head>
<body>

<div class="abs hero" role="img" aria-label="Close-up photograph of pink-tipped green succulent rosettes"></div>
<div class="abs hero-band"></div>
<div class="abs hero-brand">
  <span class="mark"></span>
  <span class="name">STILLBROOK</span>
  <span class="sub">COUNSELING</span>
</div>

<header class="abs topbar">
  <div class="abs top-brand"><span class="dot"></span>STILLBROOK</div>
  <div class="abs practitioner">Colette Brannigan, LCSW,<br>Registered Play Therapist</div>
  <ul class="abs nav">
    <li class="active">HOME</li>
    <li>ABOUT ME</li>
    <li>COUNSELING SERVICES</li>
    <li>FEES</li>
    <li>FAQS</li>
    <li>CONTACT ME</li>
  </ul>
</header>

<section class="abs welcome">
  <h1>WELCOME TO STILLBROOK COUNSELING</h1>
  <div class="rule"></div>
  <p>Lid est laborum dolo rumes fugats untras. Etharums ser quidem rerum<br>facilis dolores nemis omnis fugats vitaes nemo minima rerums unsers sadips amets.</p>
</section>

<div class="abs portrait" role="img" aria-label="Black and white portrait photograph of the therapist"></div>

<h2 class="abs section-title services-title">Services We Offer</h2>
<ul class="abs services">
  <li><svg viewBox="0 0 12 12"><circle cx="6" cy="6" r="6" fill="#0355a3"/><path d="M5 3.5 7.5 6 5 8.5" stroke="#fff" stroke-width="1.4" fill="none"/></svg>Cras rutrum leo at odio volutpat id blandit fugiats ipsum ornare.</li>
  <li><svg viewBox="0 0 12 12"><circle cx="6" cy="6" r="6" fill="#0355a3"/><path d="M5 3.5 7.5 6 5 8.5" stroke="#fff" stroke-width="1.4" fill="none"/></svg>Donec fermentum porttitor nunc, sit amet gravida est porttitor vel.</li>
  <li><svg viewBox="0 0 12 12"><circle cx="6" cy="6" r="6" fill="#0355a3"/><path d="M5 3.5 7.5 6 5 8.5" stroke="#fff" stroke-width="1.4" fill="none"/></svg>Maecenas quis nisi in uctus adipiscing sed vehicula tellus amet dolore.</li>
  <li><svg viewBox="0 0 12 12"><circle cx="6" cy="6" r="6" fill="#0355a3"/><path d="M5 3.5 7.5 6 5 8.5" stroke="#fff" stroke-width="1.4" fill="none"/></svg>Aenean faucibus sapien a odio varius aliquet voluptas sadips..</li>
  <li><svg viewBox="0 0 12 12"><circle cx="6" cy="6" r="6" fill="#0355a3"/><path d="M5 3.5 7.5 6 5 8.5" stroke="#fff" stroke-width="1.4" fill="none"/></svg>Suspendisse venenatis euismod ve vestibulum volutpat nibh imperdiets.</li>
  <li><svg viewBox="0 0 12 12"><circle cx="6" cy="6" r="6" fill="#0355a3"/><path d="M5 3.5 7.5 6 5 8.5" stroke="#fff" stroke-width="1.4" fill="none"/></svg>Quisque non leo molestie augue imperdiet sollicitudin eu nec urna.</li>
</ul>

<h2 class="abs section-title clients-title">What Client's Say</h2>
<blockquote class="abs quote">"Neque porro quisquam est, qui dolorem ipsum quia dolor sit amet, consec tetur, adipisci velit, sed quia non numquam eius modi tempora incidunt utis labore et dolore magnam aliquam quaerat voluptatem. Ut enim ad minimas veniam, quis nostrum exercitationem ullam corporis suscipit laboriosam, nisi ut aliquid ex ea commodi consequatur slores amet untras vel illum qui."</blockquote>
<div class="abs author">
  <svg width="18" height="20" viewBox="0 0 18 20"><circle cx="9" cy="5" r="4.5" fill="#5a3450"/><path d="M0 20c0-6 4-9 9-9s9 3 9 9z" fill="#5a3450"/></svg>
  <span>Jon Doe</span>
</div>

<div class="abs gap-band"></div>
<footer class="abs footer">
  <div class="abs foot-brand"><span class="dot"></span><span class="name">STILLBROOK</span><span class="sub">COUNSELING</span></div>
  <p class="abs foot-blurb">Lorem ipsum ex vix illud nonummy, novum tation et his. At vix scriptaset patrioque scribentur, at pro fugit erts verterem molestiae, sed et vivendo ali Lorem ipsum ex vix illud</p>
  <div class="abs contact">
    <h3 class="foot-heading">CONTACT</h3>
    <p>Colette Brannigan<br>2250 Fernhollow Road</p>
    <p>(208) 555-0142</p>
    <p>colette@stillbrook.example</p>
  </div>
  <nav class="abs menu">
    <h3 class="foot-heading">MENU</h3>
    <ul>
      <li>HOME</li>
      <li>ABOUT ME</li>
      <li>COUNSELING SERVICES</li>
      <li>FEES</li>
      <li>FAQs</li>
      <li>CONTACT ME</li>
      <li>BLOG</li>
    </ul>
  </nav>
</footer>

<div class="abs bottom-bar">
  <p class="abs copyright">Copyright 2016 Stillbrook Counseling | All Rights Reserved</p>
  <div class="abs social"><span></span><span></span><span></span></div>
</div>

</body>
</html>
```